Business Card Design for Technology Company

New business card design needed for technology company director.
Ideally, the design will fit the style and nature of the industry. We are a supplier of quality products and services, and we hope the design will give customers and suppliers this impression.

Target Market(s)

3D Printing Industry

Industry/Entity Type

Technology Equipment

Contact Information for Business Card

Name: Marcus Lyle
Title: Director
Company address: Factory K4, 7B Morland Road, Springvale Victoria Australia 3150
Telephone: +61-3-8555 6413
Email: marcus.lyle@veranox.com.au
Website: www.veranox.com.au

Requirements
Must have
• All information in business card details
• Company logo
• '3D Printers and 3D Print Filaments' at proper place
Nice to have
• Style to fit the industry
• Colour to fit logo

```html
<!DOCTYPE html>
<html lang="en">
<head>
<meta charset="UTF-8">
<title>Veranox Technology – Business Cards</title>
<link href="https://fonts.googleapis.com/css2?family=Roboto:wght@400;500;700;900&display=swap" rel="stylesheet">
<style>
  :root {
    --backdrop: #2b2f35;
    --card-white: #ffffff;
    --accent-yellow: #fbb829;
    --brand-blue: #1f7fc4;
    --ink: #1b1b1b;
    --ink-soft: #2a2a2a;
  }
  * { margin: 0; padding: 0; box-sizing: border-box; }
  html, body {
    width: 1200px; height: 900px; overflow: hidden;
    background: var(--backdrop);
    font-family: "Roboto", Arial, sans-serif;
    color: var(--ink);
  }
  .canvas { position: relative; width: 1200px; height: 900px; }

  .card {
    position: absolute;
    width: 540px; height: 310px;
    background: var(--card-white);
    border-radius: 4px;
    box-shadow: 0 14px 30px rgba(0,0,0,.45);
    overflow: hidden;
  }

  /* ---------- front card ---------- */
  .card--front { left: 50px; top: 470px; display: flex; }
  .front-brand {
    width: 34%;
    display: flex; flex-direction: column; align-items: center; justify-content: center; gap: 10px;
  }
  .brand-square {
    width: 44px; height: 44px; background: var(--brand-blue);
  }
  .brand-name {
    font-weight: 900; font-size: 22px; letter-spacing: 3px;
    color: var(--ink); text-align: center; line-height: 1.15;
  }
  .brand-name span { display: block; font-size: 11px; letter-spacing: 4px; }

  .front-contact {
    flex: 1; background: var(--accent-yellow);
    padding: 28px 26px 20px 30px;
    display: flex; flex-direction: column;
  }
  .person-name { color: var(--brand-blue); font-weight: 900; font-size: 26px; line-height: 1; }
  .person-title { font-weight: 500; font-size: 16px; margin-top: 4px; }
  .divider { width: 16px; height: 2px; background: var(--ink); margin: 12px 0 14px; }
  .contact-list { list-style: none; display: flex; flex-direction: column; gap: 8px; }
  .contact-list li { display: flex; align-items: center; gap: 10px; font-size: 16px; color: var(--ink-soft); }
  .contact-list svg { width: 16px; height: 16px; flex: none; }
  .tagline { margin-top: auto; font-weight: 700; font-size: 15.5px; color: var(--ink); }

  /* ---------- back card ---------- */
  .card--back { left: 620px; top: 120px; }
  .back-brand {
    position: absolute; left: 170px; top: 80px;
    display: flex; align-items: center; gap: 18px;
  }
  .back-brand .brand-square { width: 62px; height: 62px; }
  .back-brand .brand-name { font-size: 38px; text-align: left; letter-spacing: 5px; }
  .back-brand .brand-name span { font-size: 15px; letter-spacing: 8px; }
  .address {
    position: absolute; left: 26px; bottom: 26px;
    font-size: 15px; color: var(--ink-soft);
  }
</style>
</head>
<body>
<main class="canvas">

  <section class="card card--back" aria-label="Business card back">
    <div class="back-brand">
      <div class="brand-square"></div>
      <div class="brand-name">VERANOX<span>TECHNOLOGY</span></div>
    </div>
    <p class="address">Factory K4, 7B Morland Road, Springvale Victoria Australia 3150</p>
  </section>

  <section class="card card--front" aria-label="Business card front">
    <div class="front-brand">
      <div class="brand-square"></div>
      <div class="brand-name">VERANOX<span>TECHNOLOGY</span></div>
    </div>
    <div class="front-contact">
      <h1 class="person-name">MARCUS LYLE</h1>
      <p class="person-title">DIRECTOR</p>
      <div class="divider"></div>
      <ul class="contact-list">
        <li>
          <svg viewBox="0 0 24 24" aria-hidden="true"><path fill="#1f7fc4" d="M6.6 10.8a15.1 15.1 0 0 0 6.6 6.6l2.2-2.2c.3-.3.7-.4 1-.2 1.1.4 2.3.6 3.6.6.6 0 1 .4 1 1V20c0 .6-.4 1-1 1A17 17 0 0 1 3 4c0-.6.4-1 1-1h3.5c.6 0 1 .4 1 1 0 1.3.2 2.5.6 3.6.1.3 0 .7-.2 1z"/></svg>
          +61-3-8555 6413
        </li>
        <li>
          <svg viewBox="0 0 24 24" aria-hidden="true"><rect x="2" y="5" width="20" height="14" fill="#1f7fc4"/><path d="M2 5l10 8 10-8" fill="none" stroke="#fbb829" stroke-width="1.6"/></svg>
          marcus.lyle@veranox.com.au
        </li>
        <li>
          <svg viewBox="0 0 24 24" aria-hidden="true"><g fill="none" stroke="#1f7fc4" stroke-width="2"><circle cx="12" cy="12" r="9"/><ellipse cx="12" cy="12" rx="4" ry="9"/><path d="M3 12h18M5 7h14M5 17h14"/></g></svg>
          www.veranox.com.au
        </li>
      </ul>
      <p class="tagline">3D Printers and 3D Print Filaments</p>
    </div>
  </section>

</main>
</body>
</html>
```